Pest Control Company needs business card!

Hi there, we need a business card designed for our new Pest Control Company. Ideally this card will be simple, yet feel elegant and high end. We want to use the colours Orange, Black and White. Please see our attached logo for the exact colours.

Business card details:

Phone - 0461 275 804
Name - Gavin Holloway
Email - Info@steadfastverminguard.com.au

We would also like to include the following list with dot points:

SERVICES / INSPECTIONS

Termites, Wood Borers, Ants, Cockroaches, Spiders, Fleas, Mice, Rats, Bed Bugs, & More!

```html
<!DOCTYPE html>
<html lang="en">
<head>
<meta charset="utf-8">
<title>Steadfast Vermin Guard – Business Card</title>
<link href="https://fonts.googleapis.com/css2?family=Montserrat:wght@800&family=Roboto:wght@400;500;700&display=swap" rel="stylesheet">
<style>
  :root {
    --orange: #f5821f;
    --red: #e3262b;
    --black: #231f20;
    --ink: #2a2a2a;
    --white: #ffffff;
    --backdrop: #1b1b1b;
  }
  * { box-sizing: border-box; margin: 0; padding: 0; }
  html, body { width: 1200px; height: 939px; overflow: hidden; }
  body {
    background: var(--backdrop);
    font-family: "Roboto", Arial, sans-serif;
    display: flex;
    align-items: center;
    justify-content: center;
    gap: 40px;
  }
  .card {
    position: relative;
    width: 520px;
    height: 318px;
    border-radius: 18px;
    border-bottom: 5px solid var(--orange);
    overflow: hidden;
  }
  .card--front { background: var(--white); color: var(--ink); }
  .card--back {
    background: var(--black);
    display: flex;
    align-items: center;
    justify-content: center;
  }
  .brand-name {
    font-family: "Montserrat", Arial, sans-serif;
    font-weight: 800;
    text-transform: uppercase;
    line-height: 0.95;
    letter-spacing: -0.5px;
  }
  .card--front .brand-name {
    position: absolute;
    left: 34px;
    top: 48px;
    font-size: 30px;
    color: var(--black);
  }
  .card--back .brand-name {
    font-size: 46px;
    color: var(--white);
    text-align: center;
  }
  .person {
    position: absolute;
    left: 34px;
    top: 168px;
  }
  .person__name {
    font-family: "Montserrat", Arial, sans-serif;
    font-weight: 800;
    font-size: 19px;
    color: var(--red);
    text-transform: uppercase;
  }
  .person__title { font-size: 14px; margin-top: 2px; }
  .contacts {
    position: absolute;
    left: 34px;
    top: 226px;
    list-style: none;
    font-size: 13px;
    line-height: 19px;
  }
  .contacts li { display: flex; align-items: center; gap: 7px; }
  .contacts svg { width: 10px; height: 10px; fill: var(--orange); flex: none; }
  .services {
    position: absolute;
    right: 30px;
    top: 30px;
    text-align: right;
  }
  .services__heading {
    font-family: "Montserrat", Arial, sans-serif;
    font-weight: 800;
    font-size: 16px;
    color: var(--orange);
    margin-bottom: 4px;
  }
  .services__list { list-style: none; font-size: 13.5px; line-height: 20px; }
  .services__list li::after {
    content: "";
    display: inline-block;
    width: 5px;
    height: 5px;
    margin-left: 5px;
    border-radius: 50%;
    background: var(--orange);
    vertical-align: middle;
  }
</style>
</head>
<body>
  <section class="card card--front">
    <div class="brand-name">Steadfast<br>Vermin<br>Guard</div>

    <div class="person">
      <div class="person__name">Gavin Holloway</div>
      <div class="person__title">Founder &amp; CEO</div>
    </div>

    <ul class="contacts">
      <li>
        <svg viewBox="0 0 10 10"><path d="M2 0.5l1.6 2-0.9 1.1c0.6 1.3 1.5 2.2 2.7 2.7l1.1-0.9 2 1.6-0.9 1.9C4.2 8.6 1.4 5.8 0.1 2.4z"/></svg>
        0461 275 804
      </li>
      <li>
        <svg viewBox="0 0 10 10"><path d="M0 2h10v6H0z M0 2l5 3.5 5-3.5" stroke="#fff" stroke-width="0.8"/></svg>
        Info@steadfastverminguard.com.au
      </li>
      <li>
        <svg viewBox="0 0 10 10"><circle cx="5" cy="5" r="5"/></svg>
        www.steadfastverminguard.com.au
      </li>
    </ul>

    <div class="services">
      <div class="services__heading">SERVICES</div>
      <ul class="services__list">
        <li>Termites</li>
        <li>Wood Borers</li>
        <li>Ants</li>
        <li>Cockroaches</li>
        <li>Spiders</li>
        <li>Fleas</li>
        <li>Mice</li>
        <li>Rats</li>
        <li>Bed Bugs</li>
        <li>More!</li>
      </ul>
    </div>
  </section>

  <section class="card card--back">
    <div class="brand-name">Steadfast<br>Vermin<br>Guard</div>
  </section>
</body>
</html>
```